Wireless Internet Service Provider website design

We need a Internet Service Provider website that show the packages that we offer as well as the functionality where customers have the option of clicking on the various packages and be linked to a page where they can sign up for our services.
We need about 10-15 pages.
A. Integrated online store.
B. Live chat.
C. Social media page
My old website. Brindleport.nyc

Example: http://quarrylinknet.com/services/residential/ Added Tuesday, June 7, 2016

Target Market(s)

Residential and small businesses

Industry/Entity Type

Internet

Coding

Coded - Design and coding required

Number of Pages Required

5+ page

Font styles to use
Serif
Sans Serif
Script

Colors
3176b5
85cae6
ffffff

Requirements
Must have
• Online store and live chat, drop down details on pricing from current website
Nice to have
• great design, functional website,

```html
<!DOCTYPE html>
<html lang="en">
<head>
<meta charset="utf-8">
<title>Brindleport — Wireless Internet</title>
<link href="https://fonts.googleapis.com/css2?family=Montserrat:wght@600;700&family=Roboto:wght@300;400;500;700&display=swap" rel="stylesheet">
<style>
:root{
  --blue-deep:#0b5aa6;
  --blue:#3176b5;
  --blue-mid:#2a87d6;
  --blue-soft:#6fbbe9;
  --sky:#85cae6;
  --teal:#2fb3d6;
  --yellow:#f5bf2a;
  --ink:#2b2f36;
  --muted:#6b717a;
  --line:#e6e9ee;
  --panel:#f4f5f7;
  --footer:#112c48;
  --white:#ffffff;
}
*{box-sizing:border-box;margin:0;padding:0}
html,body{width:1200px;height:3051px;overflow:hidden}
body{position:relative;font-family:'Roboto',Arial,sans-serif;color:var(--ink);background:var(--white)}
.abs{position:absolute}

/* header + hero */
.hero{left:0;top:0;width:1200px;height:580px;background:linear-gradient(160deg,#5f7d92 0%,#3f5f78 40%,#6b8aa0 70%,#2e4a62 100%)}
.hero::after{content:"";position:absolute;inset:0;background:rgba(20,50,80,.35)}
.nav{left:85px;top:30px;width:1030px;height:40px;display:flex;align-items:center;z-index:2}
.brand{display:flex;align-items:center;gap:10px;color:var(--white);font-weight:700;font-size:22px}
.brand-dot{width:22px;height:22px;border-radius:50%;background:var(--sky)}
.menu{margin-left:auto;display:flex;align-items:center;gap:32px;font-size:11px;font-weight:700;color:var(--white);letter-spacing:.3px}
.menu .phone{color:var(--sky)}
.hero-copy{left:0;top:208px;width:1200px;text-align:center;color:var(--white);z-index:2}
.hero-title{font-family:'Montserrat',Arial,sans-serif;font-weight:700;font-size:30px;line-height:36px;letter-spacing:.5px}
.hero-sub{margin:14px auto 0;width:520px;font-size:15px;line-height:22px}
.btn{display:inline-block;background:var(--yellow);color:var(--white);font-weight:700;border-radius:24px;text-align:center}
.hero-btn{margin-top:24px;width:203px;height:47px;line-height:47px;font-size:14px}

/* service tiles */
.tiles{left:85px;top:543px;width:1028px;height:236px;display:flex;z-index:3}
.tile{flex:1;position:relative;padding:76px 0 0 30px;color:var(--white)}
.tile-res{background:linear-gradient(135deg,#1565b8,#1d6fc0)}
.tile-biz{background:linear-gradient(135deg,#2a7fc8,#3b92d6)}
.tile-unl{background:linear-gradient(135deg,#2fb3d6,#3cc0de)}
.tile-label{margin-top:14px;font-size:22px;font-weight:300;line-height:26px}

/* features */
.perks{left:85px;top:834px;width:474px;height:146px;background:var(--panel);display:flex;justify-content:space-around;padding-top:30px}
.perk{width:120px;text-align:center;font-size:11px;font-weight:500;line-height:15px}
.perk svg{display:block;margin:0 auto 8px}
.speed{left:616px;top:842px;width:480px}
.speed-head{display:flex;gap:18px}
.speed-title{font-size:19px;font-weight:500;line-height:24px}
.speed-text{margin:12px 0 0 40px;font-size:11.5px;line-height:19px;color:var(--muted)}
.rule{left:85px;top:1033px;width:1028px;height:2px;background:var(--line)}

/* plans */
.sec-title{width:1200px;left:0;text-align:center;font-size:28px;font-weight:400}
.sec-bar{left:570px;width:60px;height:5px;background:var(--blue-deep)}
.plans-intro{left:0;top:1172px;width:1200px;text-align:center;font-size:12.5px;line-height:21px;color:var(--muted)}
.plans{left:189px;top:1285px;width:810px;height:363px;display:flex}
.plan{width:203px;background:var(--white);border:1px solid var(--line);text-align:center;position:relative}
.plan-featured{margin-top:-8px;height:379px;box-shadow:0 6px 20px rgba(0,0,0,.12);z-index:2}
.plan-head{height:55px;line-height:55px;color:var(--white);font-size:14px;font-weight:500}
.plan-featured .plan-head{height:55px}
.h1{background:#1564b0}.h2{background:var(--blue-mid)}.h3{background:#3d98e0}.h4{background:var(--blue-soft)}
.plan-price{height:80px;background:var(--panel);padding-top:18px}
.amount{font-size:26px;font-weight:700}
.amount sup{font-size:12px;vertical-align:top;position:relative;top:6px}
.term{font-size:9px;color:var(--muted)}
.plan-list{padding-top:26px;font-size:11px;line-height:20.5px}
.plan-list b{font-weight:700}
.plan-btn{position:absolute;left:44px;bottom:24px;width:115px;height:30px;line-height:30px;font-size:10px}
.plan-featured .plan-btn{bottom:32px}

/* reviews */
.reviews{left:0;top:1739px;width:1200px;height:600px;background:linear-gradient(#edf1f6,#e6ecf3)}
.review-side{top:1980px;width:310px;height:180px;background:rgba(255,255,255,.55);text-align:center;padding-top:50px;color:#b3bac4;font-size:9px;line-height:14px}
.review-side .pill{display:inline-block;margin-top:14px;width:68px;height:18px;border-radius:9px;background:#f3e3b0}
.review-card{left:358px;top:1928px;width:504px;height:356px;background:var(--white);box-shadow:0 10px 30px rgba(0,0,0,.06);text-align:center;padding-top:78px}
.avatar{left:560px;top:1900px;width:80px;height:80px;border-radius:50%;background:#c9cdd2;border:5px solid var(--white)}
.avatar-sm{width:40px;height:40px;border-radius:50%;background:#dfe2e6}
.reviewer{font-size:16px;font-weight:700}
.origin{font-size:11px;color:var(--muted);margin-top:4px}
.quote{width:360px;margin:18px auto 0;font-size:13px;line-height:21px;color:#444}
.case-btn{margin-top:20px;width:130px;height:40px;line-height:40px;font-size:12px}
.arrow{width:54px;height:54px;border-radius:50%;top:2044px}
.arrow-prev{left:278px;background:#d7dde5}
.arrow-next{left:895px;background:#b4bfcc}

/* map + cta + footer */
.map{left:0;top:2339px;width:1200px;height:330px;background:linear-gradient(120deg,#1f4a5e,#2c5d72 45%,#1c4356)}
.cta{left:0;top:2669px;width:1200px;height:132px;background:var(--blue-deep);display:flex;align-items:center;justify-content:center;gap:28px;color:var(--white)}
.cta-text{font-size:21px;font-weight:300}
.cta-btn{width:230px;height:50px;line-height:50px;font-size:14px}
.cta-chat{width:150px;height:50px;line-height:48px;border:1.5px solid rgba(255,255,255,.5);border-radius:25px;text-align:center;font-size:14px;font-weight:700}
.footer{left:0;top:2801px;width:1200px;height:250px;background:var(--footer);color:#c6d1dd;font-size:11px;line-height:20px}
.f-brand{left:96px;top:60px}
.f-brand .brand{font-size:15px}
.f-copy{margin-top:6px;font-size:10px}
.f-col{top:58px}
.f-col h4{color:var(--white);font-size:13px;font-weight:700;margin-bottom:10px}
</style>
</head>
<body>

<div class="abs hero" role="img" aria-label="Photo of a laptop and potted plants on a desk in a bright living room"></div>

<header class="abs nav">
  <div class="brand"><span class="brand-dot"></span>Brindleport</div>
  <nav class="menu">
    <span>HOME</span><span>WHY BRINDLEPORT</span><span>PLANS &amp; PACKAGES &#8964;</span><span>GALLERY</span><span>CONTACTS</span><span class="phone">(866) 555-0148</span>
    <svg width="18" height="16" viewBox="0 0 18 16" fill="#fff"><path d="M0 1h3l3 9h9l2-7H5" fill="none" stroke="#fff" stroke-width="1.8"/><circle cx="7" cy="14" r="1.6"/><circle cx="14" cy="14" r="1.6"/></svg>
  </nav>
</header>

<section class="abs hero-copy">
  <h1 class="hero-title">LOCALLY OWN . RELIABLE .<br>SUPER FAST INTERNET .</h1>
  <p class="hero-sub">Welcome to Brindleport's fiber-speed network without fiber – the new choice for those of you who don't feel you have a lot of choices.</p>
  <span class="btn hero-btn">Request a Free Quote</span>
</section>

<section class="abs tiles">
  <div class="tile tile-res" role="img" aria-label="Home photo under a blue overlay">
    <svg width="40" height="40" viewBox="0 0 40 40" fill="none" stroke="#fff" stroke-width="2"><path d="M4 20 20 6l16 14M9 16v18h22V16M17 34V24h6v10"/></svg>
    <div class="tile-label">Residential Internet<br>Access</div>
  </div>
  <div class="tile tile-biz" role="img" aria-label="Office team photo under a blue overlay">
    <svg width="40" height="40" viewBox="0 0 40 40" fill="none" stroke="#fff" stroke-width="2"><path d="M8 36V10h14v26M22 16h10v20M4 36h32M12 15h6M12 21h6M12 27h6M26 22h3M26 28h3"/></svg>
    <div class="tile-label">Business Internet<br>Access</div>
  </div>
  <div class="tile tile-unl" role="img" aria-label="Transmission tower photo under a teal overlay">
    <svg width="40" height="40" viewBox="0 0 40 40" fill="none" stroke="#fff" stroke-width="2"><circle cx="20" cy="20" r="15"/><path d="M20 10v10l6 5"/></svg>
    <div class="tile-label">Unlimited Internet<br>Usage</div>
  </div>
</section>

<section class="abs perks">
  <div class="perk">
    <svg width="40" height="40" viewBox="0 0 40 40" fill="none" stroke="#3176b5" stroke-width="2"><circle cx="20" cy="15" r="8"/><path d="M8 36c2-8 22-8 24 0M12 15a8 8 0 0 1 16 0"/></svg>
    Customer Support<br>Center
  </div>
  <div class="perk">
    <svg width="40" height="40" viewBox="0 0 40 40" fill="none" stroke="#3176b5" stroke-width="2"><rect x="5" y="22" width="30" height="10" rx="2"/><path d="M12 22V10M28 22V10M14 8a8 8 0 0 1 12 0"/><circle cx="11" cy="27" r="1" fill="#3176b5"/><circle cx="16" cy="27" r="1" fill="#3176b5"/></svg>
    Equipment Options
  </div>
  <div class="perk">
    <svg width="40" height="40" viewBox="0 0 40 40" fill="none" stroke="#3176b5" stroke-width="2"><circle cx="20" cy="20" r="16"/><circle cx="20" cy="20" r="12" stroke-dasharray="2 2"/><text x="20" y="24" font-size="10" font-family="Roboto,sans-serif" text-anchor="middle" fill="#3176b5" stroke="none" font-weight="700">100</text></svg>
    Customer Guarantee
  </div>
</section>

<section class="abs speed">
  <div class="speed-head">
    <svg width="22" height="30" viewBox="0 0 22 30" fill="none" stroke="#3176b5" stroke-width="2"><path d="M11 12v18M5 4a9 9 0 0 0 0 12M17 4a9 9 0 0 1 0 12M8 7a5 5 0 0 0 0 6M14 7a5 5 0 0 1 0 6"/></svg>
    <h2 class="speed-title">Fast download &amp; upload<br>speeds at an affordable price</h2>
  </div>
  <p class="speed-text">When choosing among the best high speed Internet providers, there are several other factors that should be taken into consideration besides just the available download speeds. Upload speeds are important as well, though they probably are not as crucial as download speeds.</p>
</section>

<div class="abs rule"></div>

<h2 class="abs sec-title" style="top:1090px">Plan We Offer</h2>
<div class="abs sec-bar" style="top:1146px"></div>
<p class="abs plans-intro">Brindleport has a range of affordable plans that provide New Yorker with the best wireless internet service.<br>Plans provide up to 500 Mbps download speeds, unlimited internet usage per month.<br>In most areas, we have plans starting at just $39.99 per month.</p>

<section class="abs plans">
  <article class="plan">
    <div class="plan-head h1">Brindleport Simplicity</div>
    <div class="plan-price"><div class="amount"><sup>$</sup>39.99</div><div class="term">MO/1 Year</div></div>
    <div class="plan-list"><b>5 Mbps</b> Download Speed<br>Free Smart Router<br>Free Internet Protection<br>Unlimited Brindleport Wi-Fi<br>access</div>
    <span class="btn plan-btn">Try It Now</span>
  </article>
  <article class="plan plan-featured">
    <div class="plan-head h2">Brindleport Value Pack</div>
    <div class="plan-price"><div class="amount"><sup>$</sup>45.95</div><div class="term">MO/1 Year</div></div>
    <div class="plan-list"><b>10 Mbps</b> Download Speed<br>Free Smart Router<br>Free Internet Protection<br>Unlimited Brindleport Wi-Fi<br>access</div>
    <span class="btn plan-btn">Try It Now</span>
  </article>
  <article class="plan">
    <div class="plan-head h3">Brindleport Super Pack</div>
    <div class="plan-price"><div class="amount"><sup>$</sup>69.99</div><div class="term">MO/1 Year</div></div>
    <div class="plan-list"><b>25 Mbps</b> Download Speed<br>Free Smart Router<br>Free Internet Protection<br>Unlimited Brindleport Wi-Fi<br>access</div>
    <span class="btn plan-btn">Try It Now</span>
  </article>
  <article class="plan">
    <div class="plan-head h4">Brindleport Speed</div>
    <div class="plan-price"><div class="amount"><sup>$</sup>89.99</div><div class="term">MO/1 Year</div></div>
    <div class="plan-list"><b>50 Mbps</b> Download Speed<br>Free Smart Router<br>Free Internet Protection<br>Unlimited Brindleport Wi-Fi<br>access</div>
    <span class="btn plan-btn">Try It Now</span>
  </article>
</section>

<section class="abs reviews"></section>
<h2 class="abs sec-title" style="top:1790px">Customer Review</h2>
<div class="abs sec-bar" style="top:1838px"></div>

<div class="abs review-side" style="left:-10px">
  <div class="avatar-sm" style="margin:-30px auto 6px" role="img" aria-label="Customer portrait"></div>
  <b>Elliot Marsh</b><br>United Kingdom<br>Claritas est etiam processus dynamicus, qui sequitur<br>mutationem consuetudium lectorum.<br><span class="pill"></span>
</div>
<div class="abs review-side" style="left:900px">
  <div class="avatar-sm" style="margin:-30px auto 6px" role="img" aria-label="Customer portrait"></div>
  <b>Elliot Marsh</b><br>United Kingdom<br>Claritas est etiam processus dynamicus, qui sequitur<br>mutationem consuetudium lectorum.<br><span class="pill"></span>
</div>

<article class="abs review-card">
  <div class="reviewer">Elliot Marsh</div>
  <div class="origin">United Kingdom</div>
  <p class="quote">Claritas est etiam processus dynamicus, qui sequitur mutationem consuetudium lectorum. Mirum est notare quam littera gothica, quam nunc putamus parum claram</p>
  <span class="btn case-btn">CASE STUDY</span>
</article>
<div class="abs avatar" role="img" aria-label="Customer portrait"></div>

<div class="abs arrow arrow-prev"><svg width="54" height="54" viewBox="0 0 54 54" fill="none" stroke="#fff" stroke-width="2.5"><path d="M33 27H21M26 21l-6 6 6 6"/></svg></div>
<div class="abs arrow arrow-next"><svg width="54" height="54" viewBox="0 0 54 54" fill="none" stroke="#fff" stroke-width="2.5"><path d="M21 27h12M28 21l6 6-6 6"/></svg></div>

<div class="abs map" role="img" aria-label="Dark street map of New York City and Long Island with a location pin in Brooklyn"></div>

<section class="abs cta">
  <span class="cta-text">Find the best deals&nbsp; in your area</span>
  <span class="btn cta-btn">Request a Free Quote</span>
  <span class="cta-text">or</span>
  <span class="cta-chat">Live Chat</span>
</section>

<footer class="abs footer">
  <div class="abs f-brand">
    <div class="brand"><span class="brand-dot"></span>Brindleport</div>
    <div class="f-copy">© Copyright 2016</div>
  </div>
  <div class="abs f-col" style="left:238px">
    <h4>Company address:</h4>
    2840 Harlow Avenue<br>2nd Fl<br>Brooklyn, NY 11238
  </div>
  <div class="abs f-col" style="left:397px;top:90px">support@brindleport.nyc<br>sale@brindleport.nyc</div>
  <div class="abs f-col" style="left:590px;top:90px;display:flex;gap:10px;align-items:center">
    <svg width="14" height="14" viewBox="0 0 14 14" fill="#c6d1dd"><path d="M3 1l2 3-1.5 1.5a8 8 0 0 0 5 5L10 9l3 2-1 2.5C6 13 1 8 .5 2z"/></svg>866-555-0148
  </div>
  <div class="abs f-col" style="left:761px">
    <h4>Quick Links</h4>
    Refer a Friend<br>Free Internet for life<br>Terms &amp; Conditions<br>Privacy Policy<br>Site Map
  </div>
  <div class="abs f-col" style="left:928px;top:90px">
    Wireless Internet Access Agreement<br>Brindleport Internet Access<br>Customer Support Center<br>Catalog
  </div>
</footer>

</body>
</html>
```